Vorlage eines Begrüßungs-Give-Aways in Herzform gesucht
Zielgruppe
Wir sind ein kleines 4-Sterne Strandhotel mit Restaurant, www.kuestenhauswellenrand.example
Unsere Zielgruppe ist derzeit stark gemischt, hauptsächlich 40-50 plus, Feriengäste, Ostseeliebhaber,
Liebhaber höherwertiger Küche, meist Paare.
Aufgabenstellung
Geplant ist die druckfertige Vorlage eines Begrüßungs-Give-Aways in Herzform mit gestanzten Löchern für einen Gummizug , in den wir unterschiedlich gefüllte Röhrchen einklemmen können und mit einer Lochung zur späteren Aufhängung des Herzens zu Hause. Das Give-Away bekommen alle anreisenden Hotel-Gäste, eventuell auch
Restaurant-Gäste.
Das Give-Away zur Begrüßung soll:
-die Gäste angenehm überraschen, zur Aktivität anregen, zur permanenten Verwendung anregen
-bei gleichbleibender Herz- und Röhrchenform durch unterschiedliche Füllmöglichkeiten trotzdem variabel sein
-aus steifem Material (z.B. Karton) gefertigt sein, damit es auch bei Aufhängung dauerhaft stabil bleibt
-bei Aufhängung auch mit unterschiedlich gefüllten Röhrchen in der gleichen Position hängen (Loch-Position)
-an unser Hotel und Restaurant erinnern, zum Wiederkommen anregen
- Interaktionsmöglichkeiten bieten, z.B. durch einen QR-Code mit Verlinkung einer Landingpage(...)
Eine erste Vorstellung wie das Herz aussehen könnte und was aus meiner Sicht darauf abgebildet sein soll ist in der beigefügten Datei abgebildet.
Das Logo ist ebenfalls als Datei beigefügt.
Grundfarbe eventuell - den dunklen Rotton in unserem Logo, Schrift in Weiß/Grau?
Ein QR-Code (soweit das die beste Lösung sein sollte) kann durch mich gestellt werden.
Wenn QR-Code, würde ich eine Herzform favorisieren
(ob das unser QR-Code Generator macht muß noch geklärt werden).
Größe etwa 20 breit / 15 hoch.

```html
<!DOCTYPE html>
<html lang="de">
<head>
<meta charset="utf-8">
<title>Begrüßungsherz – Küstenhaus Wellenrand</title>
<link rel="stylesheet" href="https://fonts.googleapis.com/css2?family=Yellowtail&family=Cinzel+Decorative:wght@400&display=swap">
<style>
  :root {
    --paper: #ffffff;
    --brand-red: #b8282b;
    --ink-light: #fbf3e6;
    --outline-red: #a92a2c;
    --outline-blue: #3d7fa0;
    --ribbon-aqua: #cdeeed;
    --square-orange: #f4ac37;
  }
  html, body {
    margin: 0;
    padding: 0;
    width: 1200px;
    height: 966px;
    overflow: hidden;
    background: var(--paper);
  }
  .sheet { display: block; width: 1200px; height: 966px; }
  .heart-outline { fill: none; stroke-width: 3; }
  .heart-outline--red { stroke: var(--outline-red); }
  .heart-outline--blue { stroke: var(--outline-blue); }
  .title-heart { fill: url(#brandRed); filter: drop-shadow(3px 4px 4px rgba(60, 0, 0, .35)); }
  .title-text {
    font-family: "Yellowtail", cursive;
    font-size: 50px;
    fill: var(--ink-light);
    text-anchor: middle;
  }
  .brand-name {
    font-family: "Cinzel Decorative", serif;
    fill: var(--ink-light);
    text-anchor: middle;
  }
  .brand-name--red { fill: var(--brand-red); }
  .bottle-glass { fill: url(#bottleTone); stroke: #c9ced2; stroke-width: 1.5; }
  .bottle-cork { fill: #a57a55; }
  .ribbon--red { fill: url(#ribbonRed); }
  .ribbon--aqua { fill: var(--ribbon-aqua); }
  .ribbon--steel { fill: url(#ribbonSteel); }
  .code-square--red { fill: url(#brandRed); }
  .code-square--orange { fill: var(--square-orange); }
  .code-square--steel { fill: url(#squareSteel); }
</style>
</head>
<body>
<svg class="sheet" viewBox="0 0 1200 966" xmlns="http://www.w3.org/2000/svg">
  <defs>
    <path id="heartPath" d="M270 88 C232 12 122 -8 52 30 C-8 66 -10 178 30 248 C82 332 200 398 270 466 C340 398 458 332 510 248 C550 178 548 66 488 30 C418 -8 308 12 270 88 Z"/>
    <symbol id="heartSymbol" viewBox="-4 -4 548 474" preserveAspectRatio="none">
      <use href="#heartPath"/>
    </symbol>
    <clipPath id="heartClip"><use href="#heartPath"/></clipPath>

    <radialGradient id="brandRed" cx="45%" cy="40%" r="70%">
      <stop offset="0" stop-color="#d83c39"/>
      <stop offset="1" stop-color="#9e2024"/>
    </radialGradient>
    <linearGradient id="bottleTone" x1="0" y1="0" x2="1" y2="1">
      <stop offset="0" stop-color="#eef1f3"/>
      <stop offset=".35" stop-color="#c0683a"/>
      <stop offset=".7" stop-color="#a24e25"/>
      <stop offset="1" stop-color="#d9dcdf"/>
    </linearGradient>
    <linearGradient id="ribbonRed" x1="0" y1="0" x2="1" y2="0">
      <stop offset="0" stop-color="#a81d22"/>
      <stop offset=".5" stop-color="#e4453f"/>
      <stop offset="1" stop-color="#a81d22"/>
    </linearGradient>
    <linearGradient id="ribbonSteel" x1="0" y1="0" x2="1" y2="0">
      <stop offset="0" stop-color="#3f7f9f"/>
      <stop offset=".5" stop-color="#cfe3ee"/>
      <stop offset="1" stop-color="#3f7f9f"/>
    </linearGradient>
    <linearGradient id="squareSteel" x1="0" y1="0" x2="1" y2="0">
      <stop offset="0" stop-color="#4c87a6"/>
      <stop offset=".55" stop-color="#e8f1f6"/>
      <stop offset="1" stop-color="#5d93b0"/>
    </linearGradient>

    <linearGradient id="patternTiles" x1="0" y1="0" x2="1" y2="1">
      <stop offset="0" stop-color="#e86d6a"/>
      <stop offset=".35" stop-color="#6fc2b3"/>
      <stop offset=".65" stop-color="#f3dc8e"/>
      <stop offset="1" stop-color="#ef8a8a"/>
    </linearGradient>
    <linearGradient id="patternStripes" x1="0" y1="0" x2="1" y2="0">
      <stop offset="0" stop-color="#f8ecd6"/>
      <stop offset=".4" stop-color="#e7d9c9"/>
      <stop offset=".7" stop-color="#f2c8bf"/>
      <stop offset="1" stop-color="#f8e6cf"/>
    </linearGradient>
    <linearGradient id="patternChevron" x1="0" y1="0" x2="1" y2="1">
      <stop offset="0" stop-color="#f58e84"/>
      <stop offset="1" stop-color="#f3a897"/>
    </linearGradient>
    <linearGradient id="patternWatercolour" x1="0" y1="0" x2="1" y2="1">
      <stop offset="0" stop-color="#c2d9ea"/>
      <stop offset=".5" stop-color="#e6eff6"/>
      <stop offset="1" stop-color="#a9c7de"/>
    </linearGradient>
  </defs>

  <!-- Herz 1: Kachelmuster -->
  <g class="giveaway giveaway--tiles" transform="translate(34 22)">
    <g role="img" aria-label="Buntes Kachelmuster mit kleinen Herzen">
      <rect width="540" height="466" fill="url(#patternTiles)" clip-path="url(#heartClip)"/>
    </g>
    <use href="#heartPath" class="heart-outline heart-outline--red"/>
    <g class="brand-badge">
      <rect x="86" y="68" width="80" height="70" rx="6" fill="url(#brandRed)"/>
      <text class="brand-name" x="126" y="108" font-size="10">Wellenrand</text>
    </g>
    <g class="title-badge" transform="rotate(6 406 174)">
      <use href="#heartSymbol" class="title-heart" x="278" y="58" width="256" height="232"/>
      <g transform="rotate(18 406 174)">
        <text class="title-text" x="404" y="158">For Dream</text>
        <text class="title-text" x="404" y="210">Holidays</text>
      </g>
    </g>
    <g class="vial" transform="rotate(-9 160 240)">
      <g role="img" aria-label="Glasröhrchen mit Korken, gefüllt mit Bernsteinstücken">
        <rect class="bottle-cork" x="140" y="130" width="40" height="26" rx="4"/>
        <rect class="bottle-glass" x="124" y="154" width="72" height="190" rx="12"/>
      </g>
      <rect class="ribbon ribbon--red" x="112" y="272" width="96" height="28" rx="3"/>
    </g>
    <rect class="code-square code-square--red" x="258" y="314" width="84" height="72" rx="8"/>
  </g>

  <!-- Herz 2: Streifen -->
  <g class="giveaway giveaway--stripes" transform="translate(646 22)">
    <g role="img" aria-label="Vertikale Pinselstreifen in Creme, Türkis, Rot, Orange und Grau">
      <rect width="540" height="466" fill="url(#patternStripes)" clip-path="url(#heartClip)"/>
    </g>
    <use href="#heartPath" class="heart-outline heart-outline--red"/>
    <g class="brand-mark">
      <text class="brand-name brand-name--red" x="120" y="118" font-size="18">Wellenrand</text>
    </g>
    <g class="title-badge" transform="rotate(6 400 172)">
      <use href="#heartSymbol" class="title-heart" x="268" y="52" width="266" height="240"/>
      <g transform="rotate(18 400 172)">
        <text class="title-text" x="398" y="156">For Dream</text>
        <text class="title-text" x="398" y="208">Holidays</text>
      </g>
    </g>
    <g class="vial" transform="rotate(-9 160 240)">
      <g role="img" aria-label="Glasröhrchen mit Korken, gefüllt mit Bernsteinstücken">
        <rect class="bottle-cork" x="140" y="130" width="40" height="26" rx="4"/>
        <rect class="bottle-glass" x="124" y="154" width="72" height="190" rx="12"/>
      </g>
      <rect class="ribbon ribbon--aqua" x="112" y="266" width="96" height="28" rx="3"/>
    </g>
    <rect class="code-square code-square--orange" x="258" y="310" width="82" height="74" rx="8"/>
  </g>

  <!-- Herz 3: Zickzack -->
  <g class="giveaway giveaway--chevron" transform="translate(48 498)">
    <g role="img" aria-label="Korallenrotes Zickzackmuster auf Creme">
      <rect width="540" height="466" fill="url(#patternChevron)" clip-path="url(#heartClip)"/>
    </g>
    <use href="#heartPath" class="heart-outline heart-outline--red"/>
    <g class="brand-heart" transform="rotate(-6 112 84)">
      <use href="#heartSymbol" class="title-heart" x="32" y="14" width="162" height="146"/>
      <text class="brand-name" x="113" y="102" font-size="16">Wellenrand</text>
    </g>
    <g class="title-badge" transform="rotate(6 410 178)">
      <use href="#heartSymbol" class="title-heart" x="278" y="62" width="264" height="236"/>
      <g transform="rotate(18 410 178)">
        <text class="title-text" x="408" y="162">For Dream</text>
        <text class="title-text" x="408" y="214">Holidays</text>
      </g>
    </g>
    <g class="vial" transform="rotate(-9 168 260)">
      <g role="img" aria-label="Glasröhrchen mit Korken, gefüllt mit Bernsteinstücken">
        <rect class="bottle-cork" x="148" y="146" width="40" height="26" rx="4"/>
        <rect class="bottle-glass" x="132" y="170" width="72" height="190" rx="12"/>
      </g>
      <rect class="ribbon ribbon--red" x="120" y="288" width="96" height="28" rx="3"/>
    </g>
    <rect class="code-square code-square--red" x="266" y="312" width="82" height="72" rx="8"/>
  </g>

  <!-- Herz 4: Aquarell blau -->
  <g class="giveaway giveaway--watercolour" transform="translate(658 490)">
    <g role="img" aria-label="Blaues Aquarell-Ornamentmuster auf Weiß">
      <rect width="540" height="466" fill="url(#patternWatercolour)" clip-path="url(#heartClip)"/>
    </g>
    <use href="#heartPath" class="heart-outline heart-outline--blue"/>
    <g class="brand-heart" transform="rotate(-6 112 84)">
      <use href="#heartSymbol" class="title-heart" x="30" y="12" width="164" height="148"/>
      <text class="brand-name" x="112" y="100" font-size="16">Wellenrand</text>
    </g>
    <g class="title-badge" transform="rotate(6 410 186)">
      <use href="#heartSymbol" class="title-heart" x="276" y="70" width="266" height="236"/>
      <g transform="rotate(18 410 186)">
        <text class="title-text" x="408" y="170">For Dream</text>
        <text class="title-text" x="408" y="222">Holidays</text>
      </g>
    </g>
    <g class="vial" transform="rotate(-9 162 262)">
      <g role="img" aria-label="Glasröhrchen mit Korken, gefüllt mit Bernsteinstücken">
        <rect class="bottle-cork" x="142" y="146" width="40" height="26" rx="4"/>
        <rect class="bottle-glass" x="126" y="170" width="72" height="190" rx="12"/>
      </g>
      <rect class="ribbon ribbon--steel" x="114" y="290" width="96" height="28" rx="3"/>
    </g>
    <rect class="code-square code-square--steel" x="266" y="302" width="84" height="80" rx="6"/>
  </g>
</svg>
</body>
</html>
```